Doctor to Patient Management Website

I need a design for a health management website that connects doctors to patients. The website will consist of: A main page mainly describing our goal, services, and initiatives towards (Who we are AKA "About Us", Our services, Contact Us, Quick Links for health tips, Language selection, Find a doctor, search bar, Member Login Section, small glossary section below with links to all entities mentioned prior, Help section (Helpful tips and tutorials, Used to request help from admin, customer service, to resolve issues or get assistance). A profile page with two types:1) Doctor Profile: Doctor Personal info (First, Last, Middle Name, Title), Clinic, Hospital Info, Department, Credentials, Years of Experience, Patients rating, #Patients seen during the current week, #Patients seen in total, Picture, Link to email doctor, Link to print doctor's profile). Tabs for "About Me", "Contact Info", "Ratings & Comments", "Documents" (To be downloaded and uploaded by patient), "Patients (List of Patients alphabetical order by name)", "Calendar" (to see doctor's availability for booking) underneath all links. 2) Patient profile: About me, Personal Info, Height, Weight, Blood Type, Age, DOB, Name, etc..., Message and email link.Picture of patient with menu made of "Personal Data", "Biometrics", "Allergies", "Illnesses", "Medications", "Medical Procedures", "Doctors" treating the patient, "Documents" (To be downloaded and uploaded by patient). Underneath all, other patients he or she is related to (For example: family member, so patient can't connect to other patients who are family members)3) Login section: New Users will have option to register using:First Name (Required), Last Name, Middle (not required), Address (Not required), City (Required), Country (Required), Email (Not required), Phone Number (Required), Choose UserName, Password, Account Type (Doctor or Patient). Once registered, they will log in using UserName, Password, and Account_Type.Curent Users will log in using UserName, Password, and Account_Type and option to retrieve username or password.Pages to include (Login Page - Registration Page - Retrieve Username and Reset Password Page)Please see link below:https://lanternpost-media.example/importance-claiming-vitalrank-quopa-zeltra/Pictures are attached to this project as an inspirationFYI: Dummy text can be used to fill in the business, services, and descriptive information. Feel free to include your own ideas in the layout, design, categories, patterns, and more to and showcase your talent. Design and pictures provided are available as source of ideas.

Target Market(s)

Age: 21+ / Family Oriented / Medical Sector / Metropolitan Area / Educated and non Educated Users

Industry/Entity Type

Health Care

Number of Pages Required

5+ page

Font styles to use
Sans Serif

Colors

Designer to choose colors to be used in the design.

Requirements
Must have
• Thin layer design
• Simple font - No serif
• Clean menu with light but solid colors (No Gradient effect)
Nice to have
• Different color themes (2 or 3) can be combined
• Sample pictures for illustration (either as an ad or to go with the flow of your design)
• Dashboard Feel (Suggested but not required)
Should not have
• Artistic fonts - with Serif
• Dark color themes

```html
<!DOCTYPE html>
<html lang="en">
<head>
<meta charset="utf-8">
<title>MediLynk – Doctor to Patient Management</title>
<link rel="stylesheet" href="https://fonts.googleapis.com/css2?family=Roboto:wght@300;400;500;700&display=swap">
<style>
  :root {
    --green: #5cc58a;
    --ink: #2b2b2b;
    --text: #555a5f;
    --muted: #8a8f94;
    --line: #e3e5e7;
    --band: #ebebeb;
    --card: #ffffff;
    --link: #4aa3df;
    --photo-mountain-a: #6d7d86;
    --photo-mountain-b: #a9b3b6;
    --photo-forest: #3f4a3a;
    --photo-office-a: #5e6664;
    --photo-office-b: #b9a98e;
  }
  * { box-sizing: border-box; margin: 0; padding: 0; }
  html, body { width: 1200px; height: 2816px; overflow: hidden; }
  body {
    position: relative;
    background: #fff;
    font-family: "Roboto", Arial, sans-serif;
    color: var(--text);
  }
  .abs { position: absolute; }

  /* header */
  .brand { left: 72px; top: 56px; display: flex; align-items: center; gap: 12px; }
  .brand-dot { width: 28px; height: 28px; border-radius: 50%; background: var(--green); }
  .brand-name { font-size: 26px; font-weight: 700; color: var(--green); letter-spacing: -0.3px; }
  .main-nav { left: 356px; top: 64px; width: 810px; display: flex; justify-content: space-between; }
  .main-nav a { font-size: 12px; font-weight: 500; color: var(--ink); text-decoration: none; letter-spacing: 0.6px; text-transform: uppercase; }

  /* shared type */
  .eyebrow { font-size: 34px; font-weight: 300; color: var(--ink); text-transform: uppercase; line-height: 1; }
  .eyebrow-sm { font-size: 32px; font-weight: 300; color: var(--ink); line-height: 1.1; }
  .heading { font-size: 42px; font-weight: 700; color: var(--ink); line-height: 1.1; }
  .body-copy { font-size: 15px; line-height: 1.55; color: var(--muted); }
  .read-more { font-size: 13px; font-weight: 700; color: var(--ink); text-transform: uppercase; letter-spacing: 0.6px; text-decoration: none; }

  /* hero */
  .hero-kicker { left: 80px; top: 168px; }
  .hero-title { left: 80px; top: 212px; font-size: 40px; }
  .hero-copy { left: 80px; top: 280px; width: 380px; }
  .hero-more { left: 80px; top: 562px; }
  .hero-photo {
    left: 520px; top: 144px; width: 680px; height: 450px;
    background: linear-gradient(170deg, var(--photo-mountain-b) 0%, var(--photo-mountain-a) 45%, var(--photo-forest) 100%);
  }
  .slider-dots { left: 580px; top: 634px; display: flex; gap: 12px; }
  .slider-dots span { width: 7px; height: 7px; border-radius: 50%; background: #c9cccf; }
  .slider-dots span.active { background: #6b7075; }

  /* services */
  .services-kicker { left: 80px; top: 692px; }
  .services-title { left: 80px; top: 730px; }
  .service-card {
    position: absolute; top: 808px; width: 320px; height: 480px;
    background: var(--card); border: 1px solid var(--line);
  }
  .service-card.featured { top: 800px; height: 496px; border: none; box-shadow: 0 10px 34px rgba(0,0,0,0.14); }
  .service-icon { position: absolute; left: 50%; top: 90px; transform: translateX(-50%); }
  .service-name { position: absolute; left: 32px; top: 264px; font-size: 26px; font-weight: 400; color: var(--ink); text-transform: uppercase; white-space: nowrap; }
  .service-name b { font-weight: 700; }
  .service-card.featured .service-name { top: 272px; }
  .service-text { position: absolute; left: 32px; top: 308px; width: 256px; font-size: 13px; line-height: 1.5; color: var(--muted); }
  .service-card.featured .service-text { top: 316px; }
  .service-foot { position: absolute; left: 0; right: 0; bottom: 0; height: 60px; border-top: 1px solid var(--line); padding: 22px 32px; }
  .service-foot a { font-size: 12px; font-weight: 700; color: var(--ink); text-transform: uppercase; letter-spacing: 0.5px; text-decoration: none; }

  /* about */
  .about-band { left: 0; top: 1360px; width: 520px; height: 624px; background: var(--band); }
  .about-kicker { left: 80px; top: 1432px; }
  .about-title { left: 80px; top: 1470px; }
  .about-copy { left: 80px; top: 1552px; width: 380px; }
  .about-more { left: 80px; top: 1814px; }
  .about-photo {
    left: 520px; top: 1352px; width: 680px; height: 624px;
    background: linear-gradient(120deg, var(--photo-office-a) 0%, #8b8d84 50%, var(--photo-office-b) 100%);
  }

  /* glossary */
  .glossary-kicker { left: 80px; top: 2052px; }
  .glossary-title { left: 80px; top: 2090px; }
  .glossary-intro { left: 80px; top: 2156px; width: 1060px; font-size: 14px; }
  .glossary-card {
    position: absolute; top: 2248px; width: 320px; height: 480px;
    background: var(--card); border: 1px solid var(--line); box-shadow: 0 4px 16px rgba(0,0,0,0.06);
    padding: 28px 32px;
  }
  .glossary-name { font-size: 26px; font-weight: 400; color: var(--ink); text-transform: uppercase; margin-bottom: 36px; }
  .glossary-name b { font-weight: 700; }
  .glossary-list { list-style: none; }
  .glossary-list li { font-size: 15px; color: var(--text); height: 41.5px; display: flex; align-items: center; white-space: pre; }
  .glossary-list li b { color: var(--ink); font-weight: 700; }
  .glossary-list li.current { color: var(--ink); }
  .glossary-list svg { margin-left: 22px; }
</style>
</head>
<body>

<header>
  <div class="brand abs"><span class="brand-dot"></span><span class="brand-name">MediLynk</span></div>
  <nav class="main-nav abs">
    <a href="#">Home</a><a href="#">About Us</a><a href="#">Glossary</a><a href="#">Contact Us</a><a href="#">Find a Doctor</a><a href="#">Sign In</a>
  </nav>
</header>

<section class="hero">
  <p class="eyebrow-sm hero-kicker abs">What makes you</p>
  <h1 class="heading hero-title abs">Dehydrated?</h1>
  <p class="body-copy hero-copy abs">Lorem ipsum dolor sit amet, consectetuer adipiscing elit, sed diam nonummy nibh euismod tincidunt laoreet. Lorem ipsum dolor sit amet, consectetuer adipiscing elit, sed diam nonummy nibh euismod. Lorem ipsum dolor sit amet, consectetuer adipiscing elit, sed diam nonummy nibh euismod. Lorem ipsum dolor sit amet, consectetuer adipiscing elit, sed diam nonummy nibh euismod tincidunt. Lorem ipsum dolor sit amet, sed diam nonummy nibh euismod.</p>
  <a class="read-more hero-more abs" href="#">Read More</a>
  <div class="hero-photo abs" role="img" aria-label="Hiker with a backpack walking toward snowy mountains through a pine forest"></div>
  <div class="slider-dots abs"><span></span><span></span><span class="active"></span><span></span></div>
</section>

<section class="services">
  <p class="eyebrow services-kicker abs">Our</p>
  <h2 class="heading services-title abs">Services</h2>

  <article class="service-card" style="left:80px">
    <svg class="service-icon" width="80" height="80" viewBox="0 0 80 80" fill="none" stroke="#9aa0a5" stroke-width="2.5" stroke-linejoin="round">
      <path d="M24 14a7 7 0 0 0-10 10 7 7 0 0 0 4 12l6-2 22 22-2 6a7 7 0 0 0 12 4 7 7 0 0 0 10-10 7 7 0 0 0-4-12l-6 2-22-22 2-6a7 7 0 0 0-12-4z"/>
    </svg>
    <h3 class="service-name"><b>Bone</b> Analysis</h3>
    <p class="service-text">Lorem ipsum dolor sit amet, consectetuer adipiscing elit, sed diam nonummy nibh euismod Lorem ipsum dolor sit amet, consectetuer</p>
    <div class="service-foot"><a href="#">View Patients</a></div>
  </article>

  <article class="service-card featured" style="left:440px">
    <svg class="service-icon" width="80" height="80" viewBox="0 0 80 80" fill="none" stroke="#9aa0a5" stroke-width="2.5" stroke-linejoin="round" stroke-linecap="round">
      <path d="M22 68V40c0-10 4-20 10-26l8-4 6 4-4 6-6 2-2 10c6-6 16-6 22 0 6 6 4 18-2 24-6 6-18 12-32 12z"/>
      <path d="M34 46c4-2 10-2 14 2"/>
    </svg>
    <h3 class="service-name"><b>Muscle</b> Toning</h3>
    <p class="service-text">Lorem ipsum dolor sit amet, consectetuer adipiscing elit, sed diam nonummy nibh euismod Lorem ipsum dolor sit amet, consectetuer</p>
    <div class="service-foot"><a href="#">View Patients</a></div>
  </article>

  <article class="service-card" style="left:800px">
    <svg class="service-icon" width="80" height="80" viewBox="0 0 80 80" fill="none" stroke="#9aa0a5" stroke-width="2.5" stroke-linejoin="round" stroke-linecap="round">
      <path d="M18 50c-6-6-6-18 0-24 4-10 16-16 28-14 12 2 20 12 20 24 0 8-4 14-10 16v12H38v-8h-8c-4 0-6-2-6-6z"/>
      <path d="M30 24c4 0 6 4 4 8M42 20c0 6 6 6 8 10M26 38c4 2 10 0 12-4M46 38c2 4 8 4 10 2"/>
    </svg>
    <h3 class="service-name"><b>Brain</b> Functioning</h3>
    <p class="service-text">Lorem ipsum dolor sit amet, consectetuer adipiscing elit, sed diam nonummy nibh euismod Lorem ipsum dolor sit amet, consectetuer</p>
    <div class="service-foot"><a href="#">View Patients</a></div>
  </article>
</section>

<section class="about">
  <div class="about-band abs"></div>
  <p class="eyebrow about-kicker abs">About</p>
  <h2 class="heading about-title abs">Us</h2>
  <p class="body-copy about-copy abs">Lorem ipsum dolor sit amet, consectetuer adipiscing elit, sed diam nonummy nibh euismod tincidunt laoreet dolore magna. Lorem ipsum dolor sit amet, consectetuer adipiscing elit, sed diam nonummy nibh euismod. Lorem ipsum dolor sit amet, consectetuer adipiscing elit, sed diam nonummy nibh euismod tincidunt laoreet. Lorem ipsum dolor sit amet, sed diam nonummy nibh euismod tincidunt laoreet dolore magna.</p>
  <a class="read-more about-more abs" href="#">Read More</a>
  <div class="about-photo abs" role="img" aria-label="Team of colleagues meeting around a table with laptops in a bright office"></div>
</section>

<section class="glossary">
  <p class="eyebrow glossary-kicker abs">Our</p>
  <h2 class="heading glossary-title abs">Glossary</h2>
  <p class="body-copy glossary-intro abs">Lorem ipsum dolor sit amet, consectetuer adipiscing elit, sed diam nonummy nibh euismod tincidunt laoreet. Lorem ipsum dolor sit amet, consectetuer adipiscing elit, sed diam nonummy nibh euismod.</p>

  <article class="glossary-card" style="left:80px">
    <h3 class="glossary-name"><b>Bone</b> Analysis</h3>
    <ul class="glossary-list">
      <li>Bone <b>Marrow</b></li>
      <li>Bone <b>Specialities</b></li>
      <li>Bone <b>Operation</b></li>
      <li class="current"><b>Bone-marrow Surgery</b><svg width="16" height="16" viewBox="0 0 16 16" fill="none" stroke="var(--link)" stroke-width="1.6"><path d="M9 2h5v5M14 2L7 9M12 10v4H2V4h4"/></svg></li>
      <li>Lean <b>Bone Therapy</b></li>
      <li>Marrow <b>Therapy</b></li>
      <li>Lean <b>Bone Therapy</b></li>
      <li>Marrow <b>Therapy</b></li>
      <li>Lost <b>Surgeon</b></li>
    </ul>
  </article>

  <article class="glossary-card" style="left:440px">
    <h3 class="glossary-name"><b>Muscle</b> Toning</h3>
    <ul class="glossary-list">
      <li>Bone <b>Marrow</b></li>
      <li>Bone <b>Specialities</b></li>
      <li>Bone <b>Operation</b></li>
      <li>Bone-marrow <b>Surgery</b></li>
      <li>Lean <b>Bone Therapy</b></li>
      <li>Marrow <b>Therapy</b></li>
      <li>Lean <b>Bone Therapy</b></li>
      <li>Marrow <b>Therapy</b></li>
      <li>Lost <b>Surgeon</b></li>
    </ul>
  </article>

  <article class="glossary-card" style="left:800px">
    <h3 class="glossary-name"><b>Brain</b> Analysis</h3>
    <ul class="glossary-list">
      <li>Bone <b>Marrow</b></li>
      <li>Bone <b>Specialities</b></li>
      <li>Bone <b>Operation</b></li>
      <li>Bone-marrow <b>Surgery</b></li>
      <li>Lean <b>Bone Therapy</b></li>
      <li>Marrow <b>Therapy</b></li>
      <li>Lean <b>Bone Therapy</b></li>
      <li>Marrow <b>Therapy</b></li>
      <li>Lost <b>Surgeon</b></li>
    </ul>
  </article>
</section>

</body>
</html>
```